Flyer-Design für 2-jährige Ausbildung in medizinischer Kosmetik gesucht
Tolle Designvorschläge, die gut die Vorgaben umgesetzt haben. Änderungswünsche und Fertigstellung erfolgten zügig und professionell. Unbedingt empfehlenswert.
Zielgruppe
2-jährige Vollzeitausbildung in Medizinische Kosmetik an einer Berufsfachschule in privater Trägerschaft (Schulgeld erforderlich, Förderung durch Bafög und der QZ möglich). Zielgruppe sind junge Frauen ab 16, die eine Ausbildung suchen.
Aufgabenstellung
Wir wünschen uns ein freches und modernes Design, das die 50-jährige Tradition der Privatschule und die klassische Schulausbildung aber trotzdem berücksichtigt.
Wünschenswert wäre die Einbindung eines zum Slogan passenden Bildes (Zeichnung oder Comics). Überwiegend in den Schulfarben gehalten (weiß, grün, grau/silber). Ein Plakat (DIN A 3) plus dazu passender Postkarte.

```html
<!DOCTYPE html>
<html lang="de">
<head>
<meta charset="utf-8">
<title>Ausbildung zur Medizinischen Kosmetikerin</title>
<link href="https://fonts.googleapis.com/css2?family=Arimo:wght@400;700&display=swap" rel="stylesheet">
<style>
  :root {
    --green-dark: #009639;
    --green-light: #6ab02f;
    --grey: #808080;
    --grey-bar: #a6a6a6;
    --white: #ffffff;
    --skin: #efd8c8;
    --brow: #b08a72;
    --shadow-teal: #3f9a88;
    --shadow-green: #2aa36c;
  }
  * { margin: 0; padding: 0; box-sizing: border-box; }
  html, body { width: 853px; height: 1200px; overflow: hidden; background: var(--white); }
  .flyer { position: relative; width: 853px; height: 1200px; font-family: "Arimo", Arial, sans-serif; color: var(--grey); overflow: hidden; }

  .brand-dot { position: absolute; left: 108px; top: 10px; width: 150px; height: 150px; border-radius: 50%; background: var(--green-light); }
  .brand-name { position: absolute; left: 274px; top: 6px; color: var(--green-light); font-weight: 700; font-size: 44px; line-height: 39px; text-transform: uppercase; letter-spacing: 1px; white-space: nowrap; }

  .rule { position: absolute; left: 3px; top: 174px; width: 850px; height: 10px; background: var(--grey-bar); }

  .hero { position: absolute; left: 3px; top: 184px; width: 850px; height: 495px;
    background: linear-gradient(180deg, var(--skin) 0%, var(--brow) 14%, var(--brow) 24%, var(--skin) 32%, var(--shadow-teal) 48%, #d9dcd6 62%, var(--shadow-green) 76%, var(--skin) 88%, var(--skin) 100%); }

  .headline { position: absolute; left: 16px; top: 696px; font-size: 39px; font-weight: 700; color: var(--grey); white-space: nowrap; }
  .headline u { text-decoration-thickness: 2px; text-underline-offset: 6px; }

  .panel-main { position: absolute; left: 3px; top: 754px; width: 850px; height: 353px; background: var(--green-dark); }
  .panel-side { position: absolute; left: 551px; top: 765px; width: 302px; height: 351px; background: var(--green-light); }
  .panel-strip { position: absolute; left: 3px; top: 1107px; width: 850px; height: 9px; background: var(--green-light); }

  .arrow { position: absolute; left: 0; top: 0; }
  .funding { position: absolute; left: 157px; top: 851px; font-size: 26px; line-height: 30px; font-weight: 700; color: var(--white); text-shadow: 1px 1px 2px rgba(0,0,0,.35); white-space: nowrap; }

  .about { position: absolute; left: 16px; top: 944px; color: var(--white); white-space: nowrap; }
  .about-title { font-size: 16px; font-weight: 700; text-decoration: underline; margin-bottom: 3px; }
  .about-text { font-size: 15px; line-height: 18px; }

  .slogan { position: absolute; left: 568px; top: 867px; transform: rotate(-24deg); transform-origin: left top; font-size: 27px; line-height: 32px; font-weight: 700; color: var(--white); text-shadow: 1px 1px 2px rgba(0,0,0,.35); white-space: nowrap; }
  .slogan span { display: block; padding-left: 4px; }

  .branches { position: absolute; left: 560px; top: 945px; list-style: none; }
  .branches li { display: flex; align-items: center; height: 55px; font-size: 52px; font-weight: 700; color: var(--white); text-shadow: 2px 2px 2px rgba(80,80,80,.6); }
  .branches li::before { content: ""; width: 44px; height: 44px; border-radius: 50%; background: var(--white); margin-right: 18px; flex: none; }

  .contact { position: absolute; top: 1128px; font-size: 20px; line-height: 24px; color: var(--grey); white-space: nowrap; }
  .contact b { font-weight: 700; }
  .contact-address { left: 18px; }
  .contact-divider { position: absolute; left: 187px; top: 1133px; width: 2px; height: 58px; background: var(--grey); }
  .contact-phone { left: 201px; top: 1152px; }
  .contact-web { left: 463px; }
</style>
</head>
<body>
<div class="flyer">
  <header>
    <span class="brand-dot"></span>
    <div class="brand-name">Lindenhof<br>Fachschule<br>für<br>Kosmetikerinnen</div>
  </header>

  <div class="rule"></div>
  <div class="hero" role="img" aria-label="Nahaufnahme eines braunen Auges mit grünem Lidschatten und geschwungener Augenbraue"></div>

  <h1 class="headline">Ausbildung zur <u>Medizinischen Kosmetikerin</u></h1>

  <div class="panel-main"></div>
  <div class="panel-side"></div>
  <div class="panel-strip"></div>

  <svg class="arrow" width="853" height="1200" viewBox="0 0 853 1200" aria-hidden="true">
    <defs>
      <linearGradient id="arrowFill" x1="0" y1="0" x2="0" y2="1">
        <stop offset="0" stop-color="#c8dcc0"/>
        <stop offset="1" stop-color="#8fc16f"/>
      </linearGradient>
    </defs>
    <polygon points="278,765 537,843 408,843 408,921 149,921 149,843 20,843" fill="url(#arrowFill)"/>
  </svg>
  <p class="funding">Bafög &amp; Staatliche<br>Förderung möglich</p>

  <section class="about">
    <h2 class="about-title">50 Jahre Tradition &amp; Erfahrung in der Ausbildung können nicht irren</h2>
    <p class="about-text">Die Lindenhof Fachschule für Kosmetikerinnen (LFfK) bildet Sie zur<br>Medizinischen Kosmetikerin aus. Unsere zweijährige Kosmetikausbildung<br>qualifiziert Sie für einen anspruchsvollen Beruf und eröffnet Ihnen viele<br>Wege in verantwortungsvolle Tätigkeiten als Kosmetikerin. Gut für unsere<br>Absolventinnen: Der Beruf der Medizinischen Kosmetikerin ist durch eine<br>Dienstleistungsmarke geschützt, sodass Fachleute sofort erkennen, dass<br>Sie eine besonders hochwertige Kosmetikausbildung absolviert haben.</p>
  </section>

  <p class="slogan">Wir machen Sie Fit<span>für drei Branchen:</span></p>

  <ul class="branches">
    <li>Beauty</li>
    <li>Health</li>
    <li>Wellness</li>
  </ul>

  <div class="contact contact-address"><b>LFfK GmbH</b><br>Kastanienstr. 21<br>10115 Berlin</div>
  <div class="contact-divider"></div>
  <div class="contact contact-phone">Tel:&nbsp;&nbsp; 030/ 555 01 23<br>Fax: 030/ 555 01 24</div>
  <div class="contact contact-web"><b>Mehr Infos unter:</b><br>www.lindenhof-kosmetikschule.de<br>kontakt@lindenhof-kosmetikschule.de</div>
</div>
</body>
</html>
```